Business Card Design

We need a business card for a new furniture company in Utah. We are introducing a fresh new concept in Utah and would like a card to reflect to buyers that they can buy quality furniture and get it NOW. I am open to just about any color scheme, but I would like something that pops.

Business

Sofa Harbor, Lenn Varcoe
41 S. East Pine Lane
Cedar Hollow Utah 84117

```html
<!DOCTYPE html>
<html lang="en">
<head>
<meta charset="utf-8">
<title>Sofa Harbor – Business Card</title>
<link rel="stylesheet" href="https://fonts.googleapis.com/css2?family=Tinos:wght@400&display=swap">
<style>
  :root {
    --page-bg: #f2f1ef;
    --card-white: #ffffff;
    --card-white-shade: #ececec;
    --gold: #c8952f;
    --gold-light: #e2b556;
    --gold-dark: #9a6b1c;
    --brown-deep: #2b211b;
    --brown-mid: #4a3a30;
    --ink: #2a1f1a;
    --text-light: #ffffff;
  }
  * { box-sizing: border-box; margin: 0; padding: 0; }
  html, body {
    width: 1200px;
    height: 900px;
    overflow: hidden;
    background: var(--page-bg);
    font-family: "Tinos", "Times New Roman", serif;
  }
  .business-card {
    position: absolute;
    left: 100px;
    top: 165px;
    width: 1000px;
    height: 570px;
    border-radius: 40px;
    overflow: hidden;
    background: var(--card-white);
    box-shadow: 0 18px 40px rgba(0,0,0,0.18);
  }
  .card-header {
    position: absolute;
    inset: 0 0 auto 0;
    height: 250px;
    background: linear-gradient(180deg, var(--card-white-shade) 0%, var(--card-white) 45%);
  }
  .brand-square {
    position: absolute;
    left: 62px;
    top: 58px;
    width: 160px;
    height: 150px;
    background: var(--gold);
  }
  .brand-name {
    position: absolute;
    left: 262px;
    top: 90px;
    font-size: 66px;
    font-weight: 400;
    letter-spacing: 2px;
    color: var(--ink);
    line-height: 1;
  }
  .gold-band {
    position: absolute;
    left: 0; right: 0;
    top: 250px;
    height: 22px;
    background: linear-gradient(180deg, var(--gold-light), var(--gold) 50%, var(--gold-dark));
  }
  .card-body {
    position: absolute;
    left: 0; right: 0;
    top: 272px;
    bottom: 0;
    background: radial-gradient(ellipse at 70% 40%, var(--brown-mid) 0%, var(--brown-deep) 75%);
  }
  .contact-block {
    position: absolute;
    left: 60px;
    top: 310px;
    color: var(--text-light);
  }
  .person-name {
    font-size: 32px;
    color: var(--gold);
    margin-bottom: 30px;
  }
  .contact-list { list-style: none; }
  .contact-list li {
    display: flex;
    align-items: center;
    font-size: 29px;
    line-height: 34px;
    height: 34px;
  }
  .contact-list .icon {
    width: 24px;
    height: 24px;
    margin-right: 14px;
    flex: none;
    fill: var(--gold);
  }
  .contact-list .no-icon { margin-left: 38px; }
</style>
</head>
<body>
  <div class="business-card">
    <div class="card-header">
      <div class="brand-square"></div>
      <div class="brand-name">Sofa Harbor</div>
    </div>
    <div class="gold-band"></div>
    <div class="card-body" role="img" aria-label="Dark brown damask wallpaper pattern"></div>

    <div class="contact-block">
      <div class="person-name">Lenn Varcoe</div>
      <ul class="contact-list">
        <li>
          <svg class="icon" viewBox="0 0 24 24" aria-hidden="true"><path d="M6.6 10.8a15 15 0 0 0 6.6 6.6l2.2-2.2a1 1 0 0 1 1-.25 11.4 11.4 0 0 0 3.6.57 1 1 0 0 1 1 1V20a1 1 0 0 1-1 1A17 17 0 0 1 3 4a1 1 0 0 1 1-1h3.5a1 1 0 0 1 1 1c0 1.25.2 2.45.57 3.57a1 1 0 0 1-.25 1z"/></svg>
          1801 555 0147
        </li>
        <li>
          <svg class="icon" viewBox="0 0 24 24" aria-hidden="true"><path d="M12 2a10 10 0 1 0 0 20 10 10 0 0 0 0-20zm6.9 6h-2.9a15.7 15.7 0 0 0-1.4-3.6A8 8 0 0 1 18.9 8zM12 4a14 14 0 0 1 1.9 4h-3.8A14 14 0 0 1 12 4zM4.3 14a8 8 0 0 1 0-4h3.4a16 16 0 0 0 0 4zm.8 2h2.9a15.7 15.7 0 0 0 1.4 3.6A8 8 0 0 1 5.1 16zM8 8H5.1a8 8 0 0 1 4.3-3.6A15.7 15.7 0 0 0 8 8zm4 12a14 14 0 0 1-1.9-4h3.8A14 14 0 0 1 12 20zm2.3-6H9.7a14.7 14.7 0 0 1 0-4h4.6a14.7 14.7 0 0 1 0 4zm.3 5.6a15.7 15.7 0 0 0 1.4-3.6h2.9a8 8 0 0 1-4.3 3.6zm1.7-5.6a16 16 0 0 0 0-4h3.4a8 8 0 0 1 0 4z"/></svg>
          www.sofaharbor.com
        </li>
        <li>
          <svg class="icon" viewBox="0 0 24 24" aria-hidden="true"><path d="M2 6a2 2 0 0 1 2-2h16a2 2 0 0 1 2 2v12a2 2 0 0 1-2 2H4a2 2 0 0 1-2-2zm2 .5V7l8 5 8-5v-.5z"/></svg>
          info@sofaharbor.com
        </li>
        <li>
          <svg class="icon" viewBox="0 0 24 24" aria-hidden="true"><path d="M12 3 2 12h3v8h5v-5h4v5h5v-8h3z"/></svg>
          41 S. East Pine Lane
        </li>
        <li><span class="no-icon">Cedar Hollow Utah 84117</span></li>
      </ul>
    </div>
  </div>
</body>
</html>
```